Velvet Basin Suites, a portable luxury restroom trailer company needs a landing page

We need a landing page for a luxury portable restroom trailer company. This should be modern, and simple - use any combination of Pantone colors: Warm Gray 1C, Black 7C, 7529c, 873C, 8003C

We rent these trailers for special events like weddings, private parties, festivals, family reunions, team building, wine tastings, beer tastings, food truck round-ups, etc.

An idea of the landing page is in the files below. Please use stock photography and placeholder text for now. The winning design will be given final content.

Requirements
Must have
• Multiple "Get Quote" buttons or a place for them to type in type of rental, how many people etc

```html
<!DOCTYPE html>
<html lang="en">
<head>
<meta charset="utf-8">
<title>Velvet Basin Suites — Luxury Portable Restroom Trailers</title>
<link href="https://fonts.googleapis.com/css2?family=Lora:wght@400;500&family=Arimo:wght@400;700&display=swap" rel="stylesheet">
<style>
  :root{
    --brown:#8c7150;
    --brown-dark:#6f5a3f;
    --charcoal:#3d3935;
    --warm-gray:#f5f4f2;
    --field:#f6f6f6;
    --text:#111;
    --muted:#555;
    --white:#fff;
  }
  *{box-sizing:border-box;margin:0;padding:0}
  html,body{width:1200px;height:4812px;overflow:hidden;background:var(--white)}
  body{position:relative;font-family:"Arimo",Arial,sans-serif;color:var(--text)}
  .abs{position:absolute}
  .serif{font-family:"Lora",Georgia,serif;font-weight:400}
  .btn{position:absolute;display:flex;align-items:center;justify-content:center;font-size:10px;font-weight:700;letter-spacing:.3px;text-transform:uppercase}
  .btn-brown{background:var(--brown);color:var(--white)}
  .btn-dark{background:var(--charcoal);color:var(--white)}
  .btn-white{background:var(--white);color:var(--text)}

  /* header */
  .site-header{left:0;top:0;width:1200px;height:93px;background:var(--white)}
  .brand{left:121px;top:30px;display:flex;align-items:center;gap:8px;color:var(--brown);font-family:"Lora",Georgia,serif;font-size:15px}
  .brand-dot{width:22px;height:22px;border-radius:50%;background:var(--brown)}
  .main-nav a{position:absolute;top:40px;font-size:10px;font-weight:700;color:var(--text);text-decoration:none}

  /* hero */
  .hero{left:0;top:93px;width:1200px;height:600px;background:linear-gradient(100deg,#e9e6df 0%,#c9c8bb 35%,#8f9a6e 60%,#5f7341 100%)}
  .hero-title{left:121px;top:170px;font-size:56px;line-height:72px;color:var(--text)}
  .hero-copy{left:121px;top:320px;width:440px;font-size:13px;line-height:16px;color:#222}
  .dots span{position:absolute;top:597px;width:10px;height:10px;border-radius:50%;background:rgba(255,255,255,.7)}

  /* section headings */
  .section-title{text-align:center;width:1200px;left:0;font-size:45px;color:var(--text)}
  .rule{height:6px;background:var(--brown);clip-path:polygon(0 50%,50% 0,100% 50%,50% 100%)}

  /* about */
  .about-copy{left:540px;top:920px;width:540px;font-size:14px;line-height:22.4px;color:#333}

  /* events */
  .event-card{position:absolute;top:1475px;width:228px}
  .event-photo{width:228px;height:164px;border-radius:22px}
  .event-title{margin-top:32px;font-size:23px}
  .event-copy{margin-top:14px;font-size:10.5px;line-height:17px;color:var(--muted)}
  .event-card .btn{position:absolute;top:379px;left:0;width:127px;height:36px}
  .arrow{font-size:26px;color:var(--text)}

  /* products */
  .product{position:absolute;width:1200px;left:0}
  .product-photo{position:absolute;width:352px;height:203px;border-radius:22px}
  .product-title{position:absolute;font-size:22px}
  .product-copy{position:absolute;width:515px;font-size:10.5px;line-height:17px;color:var(--muted)}
  .read-more{position:absolute;display:flex;align-items:center;gap:12px;font-size:13px;font-weight:700}

  /* cta band */
  .cta-title{left:0;width:1200px;text-align:center;top:3490px;font-size:48px;color:var(--white)}
  .cta-copy{left:0;width:1200px;text-align:center;top:3550px;font-size:14px;color:var(--white)}

  /* form */
  .field-label{position:absolute;font-size:10px;color:#222}
  .field{position:absolute;width:459px;height:36px;background:var(--field);font-size:10px;color:#222;display:flex;align-items:center;justify-content:space-between;padding:0 14px}
  .field.active{background:var(--white);border:1px solid #333}
  .chev{width:8px;height:8px;border-right:1.5px solid #333;border-bottom:1.5px solid #333;transform:rotate(45deg) translateY(-3px)}

  /* footer */
  .footer-heading{position:absolute;top:4520px;font-size:22px;color:var(--white);letter-spacing:.5px}
  .footer-links a{position:absolute;font-size:10px;color:var(--white);text-decoration:none}
  .social{position:absolute;top:4581px;width:30px;height:30px;border:2.5px solid var(--white);border-radius:50%}
  .copyright{left:0;width:1200px;text-align:center;top:4782px;font-size:10px;color:#ddd}
</style>
</head>
<body>

<header class="abs site-header">
  <div class="abs brand"><span class="brand-dot"></span>Velvet Basin Suites</div>
  <nav class="main-nav">
    <a style="left:412px">HOME</a>
    <a style="left:481px">ABOUT</a>
    <a style="left:558px">EVENTS</a>
    <a style="left:637px">PRODUCTS</a>
    <a style="left:735px">CONTACT</a>
  </nav>
  <div class="btn btn-brown" style="left:949px;top:28px;width:127px;height:37px">Get Quote</div>
</header>

<section class="abs hero" role="img" aria-label="Family relaxing in camp chairs beside a white motorhome on a grassy field"></section>
<h1 class="abs serif hero-title">Luxury Portable<br>Restroom Trailer</h1>
<p class="abs hero-copy">Lorem ipsum dolor sit amet, consectetur adipiscing elit. Pretium ultrices in dolor venenatis odio.</p>
<div class="btn btn-brown" style="left:121px;top:417px;width:126px;height:37px">Contact Us</div>
<div class="btn btn-white" style="left:275px;top:417px;width:125px;height:37px">Products</div>
<div class="dots"><span style="left:571px;background:#fff"></span><span style="left:593px"></span><span style="left:617px"></span></div>
<svg class="abs" style="left:0;top:600px" width="1200" height="100" viewBox="0 0 1200 100">
  <path d="M0 30 Q600 110 1200 30 L1200 100 L0 100Z" fill="#fff"/>
  <path d="M0 36 Q600 112 1200 30 Q600 150 0 36Z" fill="var(--brown)"/>
</svg>

<!-- About -->
<div class="abs rule" style="left:239px;top:815px;width:232px"></div>
<div class="abs rule" style="left:729px;top:815px;width:232px"></div>
<h2 class="abs serif section-title" style="top:788px">About Us</h2>
<svg class="abs" style="left:88px;top:869px" width="380" height="376" viewBox="0 0 380 376">
  <defs><linearGradient id="ringTone" x1="0" x2="1"><stop offset="0" stop-color="#cfc8bd"/><stop offset="1" stop-color="#8c7150"/></linearGradient></defs>
  <circle cx="190" cy="188" r="187" fill="url(#ringTone)"/>
  <circle cx="182" cy="188" r="178" fill="#fff"/>
</svg>
<div class="abs" role="img" aria-label="Friends gathered on picnic blankets outside a motorhome" style="left:122px;top:898px;width:310px;height:310px;border-radius:50%;background:linear-gradient(160deg,#9fb8c9,#cfd6d6 40%,#8c9b6a)"></div>
<p class="abs about-copy">Lorem ipsum dolor sit amet, consectetur adipiscing elit. Felis convallis dictumst risus, leo. Erat mauris, dolor sed eu. Ante lacus at at erat ultrices feugiat aliquam augue dapibus. Tellus, commodo est augue nam amet in. Sit nibh ante bibendum hac volutpat elementum mattis. Duis convallis sem proin posuere. Vitae velit cursus nec neque nibh condimentum. Nunc orci eu dolor porttitor neque, nisl et. Ipsum maecenas quis aenean arcu nec, sed vulputate nunc. Nec purus pharetra ipsum in nibh nam arcu ac. Vel a est mauris hac sed dui ultrices.</p>
<div class="btn btn-brown" style="left:540px;top:1131px;width:127px;height:37px">Get Quote</div>

<!-- Events -->
<svg class="abs" style="left:0;top:1265px" width="1200" height="735" viewBox="0 0 1200 735">
  <path d="M0 110 Q300 30 700 10 Q1050 -5 1200 60 L1200 700 Q900 620 500 690 Q150 735 0 640Z" fill="var(--warm-gray)"/>
</svg>
<div class="abs rule" style="left:265px;top:1371px;width:232px"></div>
<div class="abs rule" style="left:705px;top:1371px;width:232px"></div>
<h2 class="abs serif section-title" style="top:1344px">Events</h2>
<span class="abs arrow" style="left:58px;top:1640px">‹</span>
<span class="abs arrow" style="left:1128px;top:1640px">›</span>

<article class="event-card" style="left:121px">
  <div class="event-photo" role="img" aria-label="Glasses of red wine raised in a toast" style="background:linear-gradient(135deg,#5a2a2e,#c27a6f 50%,#e8c9b8)"></div>
  <h3 class="serif event-title">Wine Tasting</h3>
  <p class="event-copy">Lorem ipsum dolor sit amet, consectetur adipiscing elit. Felis convallis dictumst risus, leo. Erat mauris, dolor sed eu. Ante lacus at at erat ultrices feugiat aliquam augue dapibus. Tellus, commodo est augue nam amet in.</p>
  <div class="btn btn-dark">View More</div>
</article>
<article class="event-card" style="left:364px">
  <div class="event-photo" role="img" aria-label="Bridesmaids in white dresses under balloons" style="background:linear-gradient(135deg,#2f3b2a,#9aa28c 50%,#e6e1dc)"></div>
  <h3 class="serif event-title">Wedding Party</h3>
  <p class="event-copy">Lorem ipsum dolor sit amet, consectetur adipiscing elit. Felis convallis dictumst risus, leo. Erat mauris, dolor sed eu. Ante lacus at at erat ultrices feugiat aliquam augue dapibus. Tellus, commodo est augue nam amet in.</p>
  <div class="btn btn-dark">View More</div>
</article>
<article class="event-card" style="left:607px">
  <div class="event-photo" role="img" aria-label="Colourful party balloons" style="background:linear-gradient(135deg,#3aa7a0,#d94b8c 40%,#f2c94c 75%,#6bb36b)"></div>
  <h3 class="serif event-title">Birthday Party</h3>
  <p class="event-copy">Lorem ipsum dolor sit amet, consectetur adipiscing elit. Felis convallis dictumst risus, leo. Erat mauris, dolor sed eu. Ante lacus at at erat ultrices feugiat aliquam augue dapibus. Tellus, commodo est augue nam amet in.</p>
  <div class="btn btn-dark">View More</div>
</article>
<article class="event-card" style="left:849px">
  <div class="event-photo" role="img" aria-label="Friends laughing together in a green garden" style="background:linear-gradient(135deg,#2e4225,#6f8a4f 55%,#b8c49a)"></div>
  <h3 class="serif event-title">Private Party</h3>
  <p class="event-copy">Lorem ipsum dolor sit amet, consectetur adipiscing elit. Felis convallis dictumst risus, leo. Erat mauris, dolor sed eu. Ante lacus at at erat ultrices feugiat aliquam augue dapibus. Tellus, commodo est augue nam amet in.</p>
  <div class="btn btn-dark">View More</div>
</article>

<!-- Products -->
<svg class="abs" style="left:0;top:2330px" width="1200" height="1000" viewBox="0 0 1200 1000">
  <path d="M560 150 Q800 -20 1200 40 L1200 760 Q900 700 640 780 Q520 820 600 600 Q660 420 560 300Z" fill="var(--warm-gray)"/>
</svg>
<div class="abs rule" style="left:194px;top:2161px;width:232px"></div>
<div class="abs rule" style="left:776px;top:2161px;width:232px"></div>
<h2 class="abs serif section-title" style="top:2134px">Our Products</h2>

<div class="product" style="top:0">
  <h3 class="serif product-title" style="left:121px;top:2270px">The Elite</h3>
  <p class="product-copy" style="left:121px;top:2327px">Lorem ipsum dolor sit amet, consectetur adipiscing elit. Felis convallis dictumst risus, leo. Erat mauris, dolor sed eu. Ante lacus at at erat ultrices feugiat aliquam augue dapibus. Tellus, commodo est augue nam amet in.</p>
  <div class="read-more" style="left:121px;top:2411px">READ MORE <svg width="28" height="10"><path d="M0 5H26M21 1L26 5L21 9" stroke="#111" fill="none" stroke-width="1.4"/></svg></div>
  <div class="product-photo" role="img" aria-label="Vintage wood-panelled camper trailer parked in grass" style="left:727px;top:2247px;background:linear-gradient(135deg,#7c8a6a,#c49a5e 50%,#e3e1dc)"></div>
</div>
<div class="product">
  <div class="product-photo" role="img" aria-label="Silver trailer glowing at dusk beside a patio umbrella" style="left:121px;top:2501px;background:linear-gradient(180deg,#2c4f6e,#6e8aa0 50%,#3a3f3a)"></div>
  <h3 class="serif product-title" style="left:551px;top:2523px">The Embassy</h3>
  <p class="product-copy" style="left:551px;top:2580px">Lorem ipsum dolor sit amet, consectetur adipiscing elit. Felis convallis dictumst risus, leo. Erat mauris, dolor sed eu. Ante lacus at at erat ultrices feugiat aliquam augue dapibus. Tellus, commodo est augue nam amet in.</p>
  <div class="read-more" style="left:551px;top:2664px">READ MORE <svg width="28" height="10"><path d="M0 5H26M21 1L26 5L21 9" stroke="#111" fill="none" stroke-width="1.4"/></svg></div>
</div>
<div class="product">
  <h3 class="serif product-title" style="left:121px;top:2777px">The Villa</h3>
  <p class="product-copy" style="left:121px;top:2834px">Lorem ipsum dolor sit amet, consectetur adipiscing elit. Felis convallis dictumst risus, leo. Erat mauris, dolor sed eu. Ante lacus at at erat ultrices feugiat aliquam augue dapibus. Tellus, commodo est augue nam amet in.</p>
  <div class="read-more" style="left:121px;top:2918px">READ MORE <svg width="28" height="10"><path d="M0 5H26M21 1L26 5L21 9" stroke="#111" fill="none" stroke-width="1.4"/></svg></div>
  <div class="product-photo" role="img" aria-label="Long aluminium gooseneck trailer on a paved lot" style="left:727px;top:2753px;background:linear-gradient(180deg,#cfd6dc,#9da3a6 55%,#55595a)"></div>
</div>
<div class="product">
  <div class="product-photo" role="img" aria-label="White caravan parked on gravel" style="left:121px;top:3007px;background:linear-gradient(135deg,#c8a08e,#e9e2dc 50%,#8d8275)"></div>
  <h3 class="serif product-title" style="left:551px;top:3030px">The Estate</h3>
  <p class="product-copy" style="left:551px;top:3087px">Lorem ipsum dolor sit amet, consectetur adipiscing elit. Felis convallis dictumst risus, leo. Erat mauris, dolor sed eu. Ante lacus at at erat ultrices feugiat aliquam augue dapibus. Tellus, commodo est augue nam amet in.</p>
  <div class="read-more" style="left:551px;top:3171px">READ MORE <svg width="28" height="10"><path d="M0 5H26M21 1L26 5L21 9" stroke="#111" fill="none" stroke-width="1.4"/></svg></div>
</div>
<div class="btn btn-dark" style="left:536px;top:3304px;width:127px;height:36px">View All</div>

<!-- CTA band -->
<svg class="abs" style="left:0;top:3425px" width="1200" height="290" viewBox="0 0 1200 290">
  <path d="M0 70 Q600 20 1200 70 L1200 290 L0 290Z" fill="var(--charcoal)"/>
  <path d="M0 66 Q600 -14 1200 66 Q600 18 0 66Z" fill="var(--brown)"/>
</svg>
<h2 class="abs serif cta-title">Ready To Get Started</h2>
<p class="abs cta-copy">Lorem ipsum dolor sit amet, consectetur adipiscing elit. Pretium ultrices in dolor venenatis odio.</p>
<div class="btn btn-white" style="left:536px;top:3622px;width:127px;height:36px">Contact Us</div>

<!-- Contact form -->
<div class="abs rule" style="left:93px;top:3832px;width:232px"></div>
<div class="abs rule" style="left:875px;top:3832px;width:232px"></div>
<h2 class="abs serif section-title" style="top:3805px">Contact Us/Get Quote</h2>
<form>
  <label class="field-label" style="left:121px;top:3920px">First Name</label>
  <div class="field active" style="left:121px;top:3940px"><span>|</span></div>
  <div class="field" style="left:620px;top:3940px"><span>Last Name</span></div>
  <div class="field" style="left:121px;top:4000px"><span>Email Address</span></div>
  <div class="field" style="left:620px;top:4000px"><span>Phone</span></div>
  <div class="field" style="left:121px;top:4064px"><span>Type Of Event</span><i class="chev"></i></div>
  <div class="field" style="left:620px;top:4064px"><span>How Many People</span><i class="chev"></i></div>
  <div class="field" style="left:121px;top:4127px"><span>Type Of Product You Are Interested In</span><i class="chev"></i></div>
  <div class="field" style="left:620px;top:4127px"><span>When Do You Need It</span><i class="chev"></i></div>
  <div class="field" style="left:121px;top:4189px"><span>For How Long</span><i class="chev"></i></div>
  <div class="field" style="left:620px;top:4189px"><span>Where</span><i class="chev"></i></div>
  <div class="btn btn-dark" style="left:536px;top:4273px;width:127px;height:37px;font-size:11px;text-transform:none">Send</div>
</form>

<!-- Footer -->
<svg class="abs" style="left:0;top:4400px" width="1200" height="412" viewBox="0 0 1200 412">
  <path d="M0 75 Q600 20 1200 75 L1200 412 L0 412Z" fill="var(--charcoal)"/>
  <path d="M0 72 Q600 -12 1200 72 Q600 22 0 72Z" fill="var(--brown)"/>
</svg>
<h4 class="serif footer-heading" style="left:121px">QUICK LINKS</h4>
<h4 class="serif footer-heading" style="left:523px">LEGAL</h4>
<h4 class="serif footer-heading" style="left:850px">SOCIAL &nbsp;LINKS</h4>
<nav class="footer-links">
  <a style="left:121px;top:4574px">HOME</a>
  <a style="left:121px;top:4606px">ABOUT</a>
  <a style="left:121px;top:4638px">EVENTS</a>
  <a style="left:121px;top:4670px">PRODUCT</a>
  <a style="left:121px;top:4703px">CONTACT</a>
  <a style="left:523px;top:4574px">PRIVACY POLICY</a>
  <a style="left:523px;top:4606px">REFUND AND RETURNS</a>
</nav>
<span class="social" style="left:850px" role="img" aria-label="Social profile link"></span>
<span class="social" style="left:910px" role="img" aria-label="Social profile link"></span>
<span class="social" style="left:968px" role="img" aria-label="Social profile link"></span>
<p class="abs copyright">Copyright Harbor Pixel Company 2021 - Legal</p>

</body>
</html>
```